Tildens Biscuit Barn Website

I need a website for a diner/restaurant that has been established in a farming, oil and industrial community for over 15 years. The website needs to be simple in design, but that should demonstrate the mastery of skills of the designer. Our diner/restaurant is family oriented, patriotic but very rustic
Fb Address is fb.me/TildensBarn

Pictures of the restaurant

https://www.filecrate-example.net/s/qk72hdw01/Tildens_05.jpg

Pictures of About us

https://www.filecrate-example.net/sh/zm40vrt88/AboutUsPhotos

Article about Tilden's
https://www.filecrate-example.net/s/wp31nbx57/TildensBiscuitBarn1.PDF
https://www.filecrate-example.net/s/hy65lcu29/TildensBiscuitBarn2.PDF

Reason: I was slow to update with information.

Reason: I am just getting feedback to the designs posted. I wasn't sure of the limited feedback was limiting designers from submitting designs. That and running a business with 25 employees open 12 hours a day, being here 2 hours prior and 2-3 hours after makes for long days.

I've increased the first place prize and also added funds to the second and third place prizes for your effort.

I just need the files in PSD, not HTML 5 as originally requested. We can handle getting the coding part.

Ill have the contest finalized by Monday. Thanks for your patience.

Target Market(s)

Cross section of adults from 18-35 & 35-55.

Industry/Entity Type

Industrial

Font styles to use
Other font styles liked:
• ff tisa web pro or garamond premier pro

Requirements
Must have
• Must be clean, look nice and not look like an afterthought.
Nice to have
• Please see the last two documents for information about our restaurant, which was featured in our local newspaper.

```html
<!DOCTYPE html>
<html lang="en">
<head>
<meta charset="utf-8">
<title>Tilden's Biscuit Barn</title>
<link href="https://fonts.googleapis.com/css2?family=Lato:ital,wght@0,400;0,700;1,400;1,700&family=Dancing+Script:wght@600&display=swap" rel="stylesheet">
<style>
  :root {
    --red: #a50f0f;
    --red-dark: #820a0a;
    --wood: #ecdcc3;
    --wood-light: #f3e6d2;
    --panel: #f5f3f1;
    --ink: #2b2b2b;
    --text: #555;
    --muted: #777;
    --rule: #c9c4bf;
    --blue: #8ecbea;
    --blue-edge: #63b1d8;
    --green: #8dc63f;
    --green-edge: #6fa82a;
    --field: #e9e7e5;
    --brown: #3c2418;
  }
  * { box-sizing: border-box; margin: 0; padding: 0; }
  html, body { width: 942px; height: 1200px; overflow: hidden; }
  body {
    position: relative;
    background: var(--wood);
    font-family: "Lato", Arial, sans-serif;
    color: var(--text);
  }
  .abs { position: absolute; }

  /* header */
  .site-header { position: absolute; left: 0; top: 0; width: 942px; height: 88px;
    background: linear-gradient(var(--wood-light), var(--wood)); border-top: 2px solid var(--red); }
  .brand { position: absolute; left: 105px; top: 30px; display: flex; align-items: center; gap: 8px;
    font-size: 19px; font-weight: 700; color: var(--red); letter-spacing: .3px; }
  .brand-mark { width: 14px; height: 14px; background: var(--red); }
  .main-nav a { position: absolute; top: 32px; height: 29px; line-height: 29px; font-size: 14px;
    color: #333; text-decoration: none; text-transform: uppercase; }
  .main-nav .current { left: 379px; width: 68px; text-align: center; background: var(--red);
    color: #fff; border-radius: 2px; box-shadow: 0 1px 2px rgba(0,0,0,.3); }

  /* hero */
  .hero { position: absolute; left: 0; top: 88px; width: 942px; height: 345px;
    background: linear-gradient(100deg, #cfc6b8 0%, #b9a58c 30%, #7d8a3c 50%, #c9b59a 70%, #b42a22 100%); }
  .hero-script { position: absolute; font-family: "Dancing Script", cursive; color: #fff;
    text-shadow: 0 1px 3px rgba(0,0,0,.5); }
  .hero-line { position: absolute; left: 105px; font-size: 15px; color: #fff;
    text-shadow: 0 1px 3px rgba(0,0,0,.5); }
  .slider-dot { position: absolute; top: 425px; width: 17px; height: 17px; border-radius: 50%;
    background: var(--red); border: 2px solid var(--red); }
  .slider-dot.active { background: #fff; }

  /* content panel */
  .content { position: absolute; left: 85px; top: 433px; width: 772px; height: 740px; background: var(--panel); }
  .rule-dotted { position: absolute; left: 103px; width: 735px; border-top: 1px dotted #8a857f; }
  .rule-v { position: absolute; width: 0; border-left: 1px solid #e2dedb; }
  .section-title { position: absolute; font-size: 22px; font-weight: 400; color: var(--ink); }
  .section-title span { color: var(--red); }
  .portrait { position: absolute; left: 104px; top: 530px; width: 128px; height: 128px; border-radius: 50%;
    border: 6px solid #fff; box-shadow: 0 1px 4px rgba(0,0,0,.25);
    background: radial-gradient(circle at 50% 45%, #8a6a55, #2d3a4a 70%); }
  .intro { position: absolute; left: 248px; font-size: 10.5px; line-height: 14.5px; color: var(--text);
    white-space: nowrap; }
  .intro .lead { color: #8dbb3a; }
  .btn-red { position: absolute; background: var(--red); color: #fff; text-align: center; border-radius: 2px; }
  .btn-more { left: 248px; top: 651px; width: 64px; height: 25px; line-height: 25px; font-size: 13px; font-weight: 700; }
  .round-arrow { position: absolute; top: 496px; width: 17px; height: 17px; border-radius: 50%;
    background: #fff; border: 1px solid #c9c4bf; }
  .menu-tile { position: absolute; width: 103px; height: 68px; border-radius: 3px; color: #fff;
    font-size: 11px; font-weight: 700; text-align: center; box-shadow: 0 3px 4px -2px rgba(0,0,0,.25); }
  .menu-tile.blue { background: var(--blue); border: 1px solid var(--blue-edge); }
  .menu-tile.green { background: var(--green); border: 1px solid var(--green-edge); }
  .menu-tile .icon { display: block; width: 30px; height: 30px; margin: 8px auto 6px; border-radius: 50%; background: rgba(255,255,255,.85); }
  .square-arrow { position: absolute; top: 721px; width: 18px; height: 18px; background: #e4e1de; border: 1px solid #c9c4bf; }

  .dish { position: absolute; top: 754px; width: 155px; }
  .dish-photo { width: 155px; height: 96px; border: 4px solid #fff; box-shadow: 0 0 2px rgba(0,0,0,.25); }
  .dish-name { margin-top: 9px; font-size: 12px; color: #333; }
  .dish-note { margin-top: 5px; font-size: 10px; font-style: italic; color: #666; }
  .dish-price { display: inline-block; margin-top: 10px; width: 77px; height: 25px; line-height: 25px;
    background: var(--red); color: #fff; font-size: 13px; font-weight: 700; font-style: italic; text-align: center; border-radius: 2px; }

  .col-title { position: absolute; top: 990px; font-size: 16px; font-weight: 400; color: var(--ink); }
  .col-title span { color: var(--red); }
  .quote { position: absolute; left: 103px; top: 1023px; width: 192px; height: 67px; background: #e8e5e2;
    border: 1px solid #d8d4d0; border-radius: 4px; padding: 10px 10px; font-size: 10px; line-height: 14.5px;
    font-style: italic; color: #444; }
  .quote-by { position: absolute; left: 147px; top: 1098px; font-size: 10px; font-weight: 700; color: #444; }
  .link-more { position: absolute; top: 1121px; font-size: 9.5px; font-weight: 700; font-style: italic;
    color: var(--red); text-decoration: underline; }
  .field-label { position: absolute; left: 375px; font-size: 10px; font-weight: 700; color: #333; }
  .field { position: absolute; left: 373px; width: 186px; height: 23px; background: var(--field);
    border: 1px solid #d3cfcb; border-radius: 3px; }
  .contact-line { position: absolute; left: 668px; width: 175px; font-size: 10px; line-height: 15px; color: #444; }
  .contact-icon { position: absolute; left: 651px; }

  .site-footer { position: absolute; left: 0; top: 1160px; width: 942px; height: 40px; background: var(--brown);
    border-top: 2px solid #5a3a29; }
  .copyright { position: absolute; left: 105px; top: 17px; font-size: 10px; color: #eee; }
  .social { position: absolute; top: 17px; width: 16px; height: 16px; border-radius: 50%; background: #fff; }
</style>
</head>
<body>

<header class="site-header">
  <div class="brand"><span class="brand-mark"></span>Tilden's Biscuit Barn</div>
  <nav class="main-nav">
    <a class="current" href="#">Home</a>
    <a href="#" style="left:481px">About Us</a>
    <a href="#" style="left:580px">Our Menu</a>
    <a href="#" style="left:686px">News</a>
    <a href="#" style="left:756px">Contact Us</a>
  </nav>
</header>

<section class="hero" role="img" aria-label="Photo of a plated dish with grilled shrimp and fresh green salad, diner eating with a fork">
</section>
<div class="hero-script" style="left:105px;top:130px;font-size:30px">We Are</div>
<div class="hero-line" style="top:175px">Established In A Farming, Oil And</div>
<div class="hero-line" style="top:197px">Industrial Community For</div>
<div class="hero-script" style="left:150px;top:220px;font-size:28px">Over 15 Years.</div>
<span class="slider-dot" style="left:438px"></span>
<span class="slider-dot active" style="left:462px"></span>
<span class="slider-dot" style="left:486px"></span>

<main class="content"></main>

<div class="rule-dotted" style="top:468px"></div>

<h2 class="section-title" style="left:103px;top:490px">Welcome to <span>Tilden's Biscuit Barn</span></h2>
<div class="portrait" role="img" aria-label="Portrait photo of the restaurant owner"></div>
<p class="intro" style="top:532px"><span class="lead">Lorem ipsum</span> dolor sit amet, consectetur adipiscing elit. Sed luctus<br>sapien quis luctus dictum. In hac habitasse platea dictumst.</p>
<p class="intro" style="top:570px">Vestibulum volutpat tellus quis tellus dignissim, non fermentum nisi<br>euismod. Etiam elementum ligula sed sapien accumsan, vitae iaculis<br>nulla condimentum. Nam at massa ac ipsum blandit ultrices. N nunc<br>nisi, finibus vel pharetra iaculis, euismod nec elit. Aliquam auc massa<br>ut aliquam tristique, magna enim mollis elit, ac sollicitu.</p>
<a class="btn-red btn-more">More</a>

<div class="rule-v" style="left:586px;top:490px;height:190px"></div>

<h2 class="section-title" style="left:618px;top:490px"><span>Our Menu</span></h2>
<span class="round-arrow" style="left:799px"></span>
<span class="round-arrow" style="left:822px"></span>
<div class="menu-tile blue" style="left:619px;top:528px"><span class="icon" role="img" aria-label="Egg icon"></span>Four Egg Omelets</div>
<div class="menu-tile green" style="left:736px;top:528px"><span class="icon" role="img" aria-label="Frying pan icon"></span>Griddle Items</div>
<div class="menu-tile green" style="left:619px;top:608px"><span class="icon" role="img" aria-label="Plate and cutlery icon"></span>Tilden's Lunches</div>
<div class="menu-tile blue" style="left:736px;top:608px"><span class="icon" role="img" aria-label="Chef icon"></span>Kids Menu</div>

<div class="rule-dotted" style="top:703px"></div>

<h2 class="section-title" style="left:103px;top:716px;font-size:20px">Best <span>Choice</span></h2>
<span class="square-arrow" style="left:796px"></span>
<span class="square-arrow" style="left:820px"></span>

<article class="dish" style="left:103px">
  <div class="dish-photo" role="img" aria-label="Photo of pasta with greens" style="background:linear-gradient(#f4f1ea,#d9a060 60%,#f2efe8)"></div>
  <p class="dish-name">Lorem ipsum dolor sit amet</p>
  <p class="dish-note">consectetur adipiscing elit</p>
  <span class="dish-price">Price: $420</span>
</article>
<article class="dish" style="left:297px">
  <div class="dish-photo" role="img" aria-label="Photo of grilled fish with peppers" style="background:linear-gradient(#e9e4dc,#c9602e 55%,#e8e2d8)"></div>
  <p class="dish-name">Lorem ipsum dolor sit amet</p>
  <p class="dish-note">consectetur adipiscing elit</p>
  <span class="dish-price">Price: $420</span>
</article>
<article class="dish" style="left:490px">
  <div class="dish-photo" role="img" aria-label="Photo of a strawberry tart" style="background:linear-gradient(#f6f1f1,#d63a3a 45%,#e9c9a0)"></div>
  <p class="dish-name">Lorem ipsum dolor sit amet</p>
  <p class="dish-note">consectetur adipiscing elit</p>
  <span class="dish-price">Price: $420</span>
</article>
<article class="dish" style="left:684px">
  <div class="dish-photo" role="img" aria-label="Photo of grilled vegetables on polenta" style="background:linear-gradient(#f3efe7,#e5b842 55%,#e8e3da)"></div>
  <p class="dish-name">Lorem ipsum dolor sit amet</p>
  <p class="dish-note">consectetur adipiscing elit</p>
  <span class="dish-price">Price: $420</span>
</article>

<div class="rule-dotted" style="top:957px"></div>

<h3 class="col-title" style="left:105px">Client <span>Testimonial</span></h3>
<div class="quote">“ Lorem iptrsum doplor sit aym nsecte tuer adipiscing elit, sed dia nonumm y nibh euismod. ”</div>
<svg class="abs" style="left:120px;top:1089px" width="18" height="14" viewBox="0 0 18 14"><path d="M0 0 L18 0 L16 14 Z" fill="#e8e5e2" stroke="#d8d4d0"/><rect x="1" y="-1" width="16" height="2" fill="#e8e5e2"/></svg>
<p class="quote-by">Marla Oakes, 11july 2014</p>
<a class="link-more" style="left:237px">Read More»</a>

<div class="rule-v" style="left:337px;top:995px;height:120px"></div>

<h3 class="col-title" style="left:374px;top:992px">Newsletter <span>Signup</span></h3>
<label class="field-label" style="top:1022px">Your Name</label>
<div class="field" style="top:1038px"></div>
<label class="field-label" style="top:1071px">Your Email Address</label>
<div class="field" style="top:1087px"></div>
<a class="link-more" style="left:490px">Subscribe Now»</a>

<div class="rule-v" style="left:607px;top:995px;height:120px"></div>

<h3 class="col-title" style="left:648px">Contact <span>Info</span></h3>
<svg class="contact-icon" style="top:1023px" width="11" height="15" viewBox="0 0 11 15"><path d="M5.5 0 C2.5 0 0 2.4 0 5.4 C0 9 5.5 15 5.5 15 C5.5 15 11 9 11 5.4 C11 2.4 8.5 0 5.5 0 Z" fill="var(--red)"/><circle cx="5.5" cy="5.3" r="2" fill="var(--panel)"/></svg>
<p class="contact-line" style="top:1021px">Lorem ipsum dolor sit a consectetuer adipiscing elit,</p>
<svg class="contact-icon" style="top:1069px" width="13" height="13" viewBox="0 0 13 13"><path d="M2.6 0.5 L4.8 3.2 L3.6 4.8 C4.4 6.5 6.4 8.6 8.2 9.4 L9.8 8.2 L12.5 10.4 L11 12.6 C5.6 12.4 0.6 7.4 0.4 2 Z" fill="var(--red)"/></svg>
<p class="contact-line" style="top:1069px">1234-4567-890</p>
<svg class="contact-icon" style="top:1097px" width="13" height="9" viewBox="0 0 13 9"><rect width="13" height="9" fill="var(--red)"/><path d="M0 0 L6.5 5 L13 0" fill="none" stroke="var(--panel)" stroke-width="1.2"/></svg>
<p class="contact-line" style="top:1094px">info@tildensbarn-example.net</p>
<a class="link-more" style="left:786px">Contact Us»</a>

<footer class="site-footer">
  <p class="copyright">© 2014 Tilden's Biscuit Barn. | All Rights Reserved</p>
  <span class="social" style="left:750px"></span>
  <span class="social" style="left:774px"></span>
  <span class="social" style="left:798px"></span>
  <span class="social" style="left:822px"></span>
</footer>

</body>
</html>
```